Recovery Lounge

We are opening a recovering lounge in our physical therapy clinic. We would like a menu of our services that we can offer guest. We would like it to flow well with our brand. Ive attached a doc of our prices an basic idea of what we are looking for.

our website is corvaptclinic.com if your need brand inspiration.

```html
<!DOCTYPE html>
<html lang="en">
<head>
<meta charset="utf-8">
<title>Corva Recovery Lounge – Service Menu</title>
<link rel="stylesheet" href="https://fonts.googleapis.com/css2?family=Fira+Sans:ital,wght@0,400;0,600;0,700;1,300;1,400;1,600&family=Fira+Sans+Condensed:wght@700&display=swap">
<style>
  :root{
    --purple:#46318f;
    --purple-deep:#2c2263;
    --coral:#f1694b;
    --coral-dark:#e35f43;
    --white:#ffffff;
    --paper:#ffffff;
  }
  *{box-sizing:border-box;margin:0;padding:0}
  html,body{width:977px;height:1200px;overflow:hidden;background:var(--paper)}
  body{font-family:"Fira Sans",sans-serif;color:var(--white)}
  .menu{position:relative;width:977px;height:1200px;background:var(--paper);overflow:hidden}

  /* header */
  .brand{position:absolute;left:60px;top:150px;width:300px;display:flex;align-items:center;gap:14px}
  .brand-dot{width:34px;height:34px;background:var(--coral);border-radius:50%}
  .brand-name{font-weight:600;font-size:84px;color:var(--purple);line-height:1}
  .header-rule{position:absolute;left:380px;top:50px;width:2px;height:217px;background:var(--coral)}
  .headline{position:absolute;left:420px;top:73px;font-family:"Fira Sans Condensed",sans-serif;font-weight:700;font-size:98px;line-height:.86;color:var(--purple);letter-spacing:6px}

  /* backdrop band */
  .texture-band{position:absolute;left:0;top:284px;width:302px;height:844px;background:linear-gradient(160deg,var(--purple-deep) 0%,#3b2b80 45%,#4b3596 100%)}

  /* panels */
  .panel{position:absolute;right:0;background:var(--coral)}
  .panel::before{content:"";position:absolute;left:0;top:0;bottom:0;width:var(--strip);background:var(--coral-dark)}
  .panel-carte{left:128px;top:302px;height:358px;--strip:174px}
  .panel-bundles{left:124px;top:677px;height:451px;--strip:178px}

  .section-no{position:absolute;left:155px;font-weight:700;font-size:90px;line-height:1;color:var(--white)}
  .section-title{position:absolute;left:337px;font-weight:600;font-size:57px;line-height:1;color:var(--white);white-space:nowrap}
  .section-rule{position:absolute;left:267px;right:0;height:1.5px;background:rgba(255,255,255,.85)}
  .unit-note{position:absolute;right:52px;top:309px;font-style:italic;font-size:15px;letter-spacing:1.5px}

  .price-list{position:absolute;left:337px;width:588px;list-style:none}
  .row{display:flex;align-items:flex-end;white-space:nowrap}
  .item{font-weight:600;font-size:27px;line-height:1}
  .mins{font-style:italic;font-weight:300;font-size:23px}
  .leader{flex:1;border-bottom:3px dotted rgba(255,255,255,.9);margin:0 6px 5px 8px}
  .price{font-weight:700;font-size:44px;line-height:1}

  .carte-list{top:413px}
  .carte-list li{height:45px}

  .bundle-list{top:796px}
  .bundle{height:76px}
  .bundle .item{font-size:26px;letter-spacing:2.5px}
  .bundle .mins{letter-spacing:1px}
  .bundle .leader{margin-right:14px}
  .bundle .price{font-size:46px}
  .save{font-style:italic;font-size:25px;margin-left:8px;padding-bottom:4px;line-height:1}
  .contents{font-style:italic;font-weight:300;font-size:21px;line-height:1;margin-top:1px;white-space:nowrap}
  .contents b{font-weight:600}

  .footnote{position:absolute;left:0;right:0;top:1152px;text-align:center;font-style:italic;font-size:17px;letter-spacing:1.6px;color:var(--coral)}
</style>
</head>
<body>
<main class="menu">
  <header>
    <div class="brand"><span class="brand-dot"></span><span class="brand-name">corva</span></div>
    <div class="header-rule"></div>
    <h1 class="headline">RECOVERY<br>LOUNGE</h1>
  </header>

  <div class="texture-band" role="img" aria-label="Purple textured photo of the lounge interior"></div>

  <section class="panel panel-carte"></section>
  <span class="section-no" style="top:318px">01</span>
  <h2 class="section-title" style="top:328px">A La CARTE</h2>
  <div class="section-rule" style="top:396px"></div>
  <p class="unit-note">(*)Number is on Minutes</p>
  <ul class="price-list carte-list">
    <li class="row"><span class="item">Infrared Sauna + Red Light <span class="mins">(30)</span></span><span class="leader"></span><span class="price">$40</span></li>
    <li class="row"><span class="item">Infrared Sauna + Red Light <span class="mins">(60)</span></span><span class="leader"></span><span class="price">$65</span></li>
    <li class="row"><span class="item">Flowtec Compression <span class="mins">(30)</span></span><span class="leader"></span><span class="price">$40</span></li>
    <li class="row"><span class="item">Flowtec Compression <span class="mins">(60)</span></span><span class="leader"></span><span class="price">$65</span></li>
    <li class="row"><span class="item">Paraffin Hand Bath <span class="mins">(15)</span></span><span class="leader"></span><span class="price">$25</span></li>
  </ul>

  <section class="panel panel-bundles"></section>
  <span class="section-no" style="top:706px">02</span>
  <h2 class="section-title" style="top:712px">BUNDLES (best sellers)</h2>
  <div class="section-rule" style="top:782px"></div>
  <ul class="price-list bundle-list">
    <li class="bundle">
      <div class="row"><span class="item">RESET <span class="mins">(45)</span></span><span class="leader"></span><span class="price">$55</span><span class="save">- Save $10</span></div>
      <p class="contents"><b>Choose 1:</b> Sauna (30) or Flowtec (30) + Paraffin Hand Bath</p>
    </li>
    <li class="bundle">
      <div class="row"><span class="item">REFRESH <span class="mins">(60)</span></span><span class="leader"></span><span class="price">$65</span><span class="save">- Save $15</span></div>
      <p class="contents">Sauna (30) + Flowtec (30)</p>
    </li>
    <li class="bundle">
      <div class="row"><span class="item">RESTORE <span class="mins">(75)</span></span><span class="leader"></span><span class="price">$85</span><span class="save">- Save $20</span></div>
      <p class="contents">Sauna (30) + Flowtec (30) + Paraffin</p>
    </li>
    <li class="bundle">
      <div class="row"><span class="item">REJUVENATE <span class="mins">(130)</span></span><span class="leader"></span><span class="price">$130</span><span class="save">- Save $25</span></div>
      <p class="contents">Sauna (60) + Flowtec (60) + Paraffin</p>
    </li>
  </ul>

  <p class="footnote">*For safety, a rest/cool-down period is required after 30 minutes in the sauna.</p>
</main>
</body>
</html>
```